Oakridge Lamont Electric van design

Looking to design a wrap for a 2021 valdane trekkor high roof using orange black and dark grey colors like in the logo

```html
<!DOCTYPE html>
<html lang="en">
<head>
<meta charset="utf-8">
<title>Oakridge Lamont Electric – Van Wrap Side Layout</title>
<link rel="stylesheet" href="https://fonts.googleapis.com/css2?family=Montserrat:wght@600&family=Barlow+Semi+Condensed:wght@500&family=Open+Sans:wght@600;700&display=swap">
<style>
  :root {
    --canvas-grey: #454545;
    --wrap-white: #ffffff;
    --wrap-orange: #e2603d;
    --wrap-orange-soft: #e7795a;
    --wrap-black: #0b0b0b;
    --ink: #111111;
  }
  html, body {
    margin: 0;
    padding: 0;
    width: 1200px;
    height: 1010px;
    overflow: hidden;
    background: var(--canvas-grey);
  }
  .canvas {
    position: relative;
    width: 1200px;
    height: 1010px;
    background: var(--canvas-grey);
  }
  .wrap-layout {
    position: absolute;
    left: 40px;
    top: 317px;
    width: 1120px;
    height: 375px;
    display: block;
  }
  .panel-white { fill: var(--wrap-white); }
  .panel-orange { fill: var(--wrap-orange); }
  .panel-orange-soft { fill: var(--wrap-orange-soft); }
  .swoosh { fill: none; stroke: var(--wrap-black); stroke-width: 24; stroke-linecap: round; }
  .corner-black { fill: var(--wrap-black); }
  .brand-mark { fill: var(--wrap-orange); }
  .brand-name {
    font-family: "Montserrat", sans-serif;
    font-weight: 600;
    font-size: 74px;
    fill: var(--ink);
  }
  .service {
    font-family: "Barlow Semi Condensed", sans-serif;
    font-weight: 500;
    font-size: 21px;
    fill: var(--ink);
  }
  .service-arrow { fill: var(--wrap-orange); }
  .phone {
    font-family: "Open Sans", sans-serif;
    font-weight: 700;
    font-size: 40px;
    fill: var(--ink);
  }
  .web {
    font-family: "Open Sans", sans-serif;
    font-weight: 600;
    font-size: 18px;
    fill: var(--ink);
  }
</style>
</head>
<body>
<main class="canvas">
  <svg class="wrap-layout" viewBox="0 0 1790 600" xmlns="http://www.w3.org/2000/svg" aria-label="Oakridge Lamont Electric van side wrap layout">
    <defs>
      <symbol id="arrow" viewBox="0 0 20 14">
        <path class="service-arrow" d="M0 4 H11 V0 L20 7 L11 14 V10 H0 Z"/>
      </symbol>
    </defs>

    <!-- base panels -->
    <rect class="panel-white" x="0" y="0" width="1790" height="600"/>
    <path class="panel-orange"
          d="M0 435 L560 435 C1000 432 1280 420 1370 370 C1470 310 1580 130 1690 0 L1790 0 L1790 600 L0 600 Z"/>
    <rect class="panel-orange-soft" x="330" y="440" width="1460" height="160" opacity="0.35"/>

    <!-- black swoosh and corner -->
    <path class="swoosh"
          d="M540 438 C1000 432 1280 420 1370 370 C1470 310 1580 130 1690 -10"/>
    <path class="corner-black" d="M1730 0 L1790 0 L1790 440 L1790 440 Z M1700 0 L1790 0 L1790 440 Z"/>

    <!-- brand -->
    <circle class="brand-mark" cx="712" cy="155" r="92"/>
    <text class="brand-name" x="845" y="140">Oakridge Lamont</text>
    <text class="brand-name" x="845" y="222">Electric</text>

    <!-- services, column one -->
    <g class="services">
      <use href="#arrow" x="700" y="284" width="24" height="16"/>
      <text class="service" x="733" y="298">Generator Installation</text>
      <use href="#arrow" x="700" y="314" width="24" height="16"/>
      <text class="service" x="733" y="328">Service Upgrades</text>
      <use href="#arrow" x="700" y="344" width="24" height="16"/>
      <text class="service" x="733" y="358">Low Voltage Wiring</text>
      <use href="#arrow" x="700" y="374" width="24" height="16"/>
      <text class="service" x="733" y="388">3-Phase Service</text>

      <!-- services, column two -->
      <use href="#arrow" x="964" y="288" width="24" height="16"/>
      <text class="service" x="997" y="302">Equipment Connections</text>
      <use href="#arrow" x="964" y="318" width="24" height="16"/>
      <text class="service" x="997" y="332">Emergency Lighting</text>
      <use href="#arrow" x="964" y="348" width="24" height="16"/>
      <text class="service" x="997" y="362">Code Violations</text>
      <use href="#arrow" x="964" y="378" width="24" height="16"/>
      <text class="service" x="997" y="392">Warehouse Lighting</text>
    </g>

    <!-- contact -->
    <text class="phone" x="1535" y="392" text-anchor="middle">555.214.3870</text>
    <text class="web" x="1535" y="420" text-anchor="middle">www.oakridgelamontelectric.com</text>
  </svg>
</main>
</body>
</html>
```